Stockly Z5 - DL Flyer

Flyer designed with the following points:

Retail Point of Sale
Hardware and Software
Highly customisable to suit your business
Free POS appraisal and Quotes
E-commerce Integrations with your existing website
Multiple Store Capability
One on one set up and support
100% Tax Deductable
From only $9.95 per week

1300 462 718
admin@stocklyz5.com.au
www.stocklyz5.com.au

```html
<!DOCTYPE html>
<html lang="en">
<head>
<meta charset="utf-8">
<title>Stockly Z5 - DL Flyer</title>
<link href="https://fonts.googleapis.com/css2?family=Montserrat:wght@400;600;700;800;900&family=Roboto:wght@400;500;700&display=swap" rel="stylesheet">
<style>
:root{
  --blue:#1aa7e8;
  --blue-light:#4cc3f0;
  --blue-pale:#dff3fc;
  --black:#0b0b0b;
  --white:#ffffff;
  --ink:#1d1d1d;
  --page:#ffffff;
}
*{box-sizing:border-box;margin:0;padding:0}
html,body{width:1200px;height:2713px;overflow:hidden;background:var(--page)}
body{position:relative;font-family:"Roboto",sans-serif}
.flyer{position:absolute;top:836px;width:520px;height:1040px;overflow:hidden;box-shadow:0 10px 30px rgba(0,0,0,.18)}
.flyer--front{left:45px;background:var(--white)}
.flyer--back{left:635px;background:var(--blue-pale)}
.brand{position:absolute;display:flex;align-items:center;gap:8px;font-family:"Montserrat",sans-serif;font-weight:800;font-size:40px;color:var(--blue);letter-spacing:.5px}
.brand__dot{width:22px;height:22px;border-radius:50%;background:var(--blue)}
.deco-circle{position:absolute;border-radius:50%}
.illustration{position:absolute;left:30px;top:125px;width:460px;height:345px;border-radius:6px;background:linear-gradient(160deg,#f6b04a 0%,#5b8de8 45%,#2f5fd0 70%,#c9d4e8 100%)}
.band-black{position:absolute;left:0;top:340px;width:520px;height:130px;background:var(--black)}
.features{position:absolute;left:0;top:470px;width:520px;height:505px;background:linear-gradient(160deg,var(--blue-light),var(--blue))}
.feature{position:absolute;display:flex;align-items:center;gap:14px;color:var(--white);font-size:13px;line-height:1.2;width:230px}
.feature__icon{flex:none;width:52px;height:52px;border-radius:50%;background:var(--black);border:3px solid var(--white);display:flex;align-items:center;justify-content:center}
.offer{position:absolute;left:32px;top:808px;color:var(--white);font-family:"Montserrat",sans-serif}
.offer__line{display:flex;align-items:baseline;line-height:1}
.offer__from{font-size:35px;font-weight:400;letter-spacing:1px}
.offer__price{font-size:66px;font-weight:900;color:var(--black);margin-left:10px}
.offer__week{font-size:60px;font-weight:900;line-height:1;letter-spacing:1px;margin-top:4px}
.offer__rule{position:absolute;left:375px;top:928px;width:145px;height:2px;background:var(--white)}
.footer{position:absolute;left:0;bottom:0;width:520px;height:65px;background:var(--black);color:var(--white);display:flex;align-items:center;justify-content:center;gap:14px;font-size:12.5px}
.footer__item{display:flex;align-items:center;gap:6px}
.footer__icon{width:16px;height:16px}
.back-header{position:absolute;left:0;top:0;width:520px;height:155px;background:var(--black)}
.card{position:absolute;width:208px;height:360px;border-radius:16px;background:var(--blue);border:4px solid var(--white);color:var(--white)}
.card__top{position:absolute;left:6px;top:6px;width:188px;height:160px;background:var(--white);border-radius:12px}
.card__price{position:absolute;left:-12px;top:14px;width:150px;height:88px;background:var(--blue);clip-path:polygon(0 0,100% 0,93% 100%,0 100%);font-family:"Montserrat",sans-serif;color:var(--black)}
.card__amount{position:absolute;left:32px;top:0;font-size:52px;font-weight:800;line-height:1.1}
.card__amount sup{font-size:28px;vertical-align:top;position:relative;top:4px}
.card__cur{position:absolute;left:18px;top:44px;font-size:13px;font-weight:700}
.card__per{position:absolute;left:32px;top:64px;font-size:14px;font-weight:600;color:var(--white)}
.card__name{position:absolute;left:0;top:112px;width:188px;text-align:center;color:var(--black)}
.card__title{font-family:"Montserrat",sans-serif;font-weight:600;font-size:19px;line-height:1}
.card__sub{font-size:12px;letter-spacing:.3px}
.card__list{position:absolute;left:14px;top:178px;width:172px;list-style:none}
.card__list li{display:flex;align-items:center;gap:10px;font-size:12px;padding:6px 6px;border-bottom:1.5px solid var(--white)}
.tick{width:13px;height:13px;flex:none}
.card__buy{position:absolute;left:30px;top:282px;width:140px;height:28px;background:var(--white);border-radius:4px;color:var(--black);font-family:"Montserrat",sans-serif;font-weight:600;font-size:18px;text-align:center;line-height:28px}
.card__tax{position:absolute;left:0;top:318px;width:200px;text-align:center;font-size:12px;line-height:1.1}
</style>
</head>
<body>

<section class="flyer flyer--front">
  <div class="deco-circle" style="left:345px;top:30px;width:170px;height:170px;background:#e3f4fc"></div>
  <div class="brand" style="left:38px;top:42px"><span>STOCKLY Z5</span><span class="brand__dot"></span></div>
  <div class="band-black"></div>
  <div class="illustration" role="img" aria-label="Illustration of shop staff and customers around a large point of sale screen with a globe, sale tags and delivery truck"></div>

  <div class="features">
    <div class="feature" style="left:32px;top:30px"><span class="feature__icon"><svg width="24" height="24" viewBox="0 0 24 24" fill="none" stroke="#fff" stroke-width="2"><rect x="4" y="10" width="16" height="10"/><rect x="7" y="4" width="10" height="6"/></svg></span>Retail Point of Sale</div>
    <div class="feature" style="left:282px;top:30px"><span class="feature__icon"><svg width="24" height="24" viewBox="0 0 24 24" fill="none" stroke="#fff" stroke-width="2"><rect x="3" y="4" width="18" height="12"/><circle cx="15" cy="16" r="4"/></svg></span>Hardware and<br>Software</div>
    <div class="feature" style="left:32px;top:105px"><span class="feature__icon"><svg width="24" height="24" viewBox="0 0 24 24" fill="none" stroke="#fff" stroke-width="2"><rect x="3" y="4" width="18" height="15"/><circle cx="12" cy="13" r="3"/></svg></span>Highly customisable<br>to suit your business</div>
    <div class="feature" style="left:282px;top:105px"><span class="feature__icon"><svg width="24" height="24" viewBox="0 0 24 24" fill="none" stroke="#fff" stroke-width="2"><rect x="5" y="11" width="14" height="9"/><rect x="8" y="4" width="8" height="5"/></svg></span>Free POS appraisal<br>and Quotes</div>
    <div class="feature" style="left:32px;top:180px"><span class="feature__icon"><svg width="24" height="24" viewBox="0 0 24 24" fill="none" stroke="#fff" stroke-width="2"><circle cx="9" cy="10" r="4"/><circle cx="16" cy="16" r="3"/></svg></span>One on one set<br>up and support</div>
    <div class="feature" style="left:282px;top:180px"><span class="feature__icon"><svg width="24" height="24" viewBox="0 0 24 24" fill="none" stroke="#fff" stroke-width="2"><path d="M4 10h16l-2-5H6z"/><rect x="5" y="10" width="14" height="10"/></svg></span>Multiple Store<br>Capability</div>
    <div class="feature" style="left:32px;top:255px"><span class="feature__icon"><svg width="24" height="24" viewBox="0 0 24 24" fill="none" stroke="#fff" stroke-width="2"><rect x="3" y="4" width="18" height="12"/><path d="M12 16v4M8 20h8"/></svg></span>E-commerce<br>Integrations with<br>your existing website</div>
    <div class="feature" style="left:282px;top:255px"><span class="feature__icon"><svg width="24" height="24" viewBox="0 0 24 24" fill="none" stroke="#fff" stroke-width="2"><rect x="4" y="3" width="16" height="18"/><path d="M8 14h8"/></svg></span>100% Tax<br>Deductable</div>
  </div>

  <div class="offer">
    <div class="offer__line"><span class="offer__from">FROM ONLY</span><span class="offer__price">$9.95</span></div>
    <div class="offer__week">PER WEEK</div>
  </div>
  <div class="offer__rule"></div>

  <footer class="footer">
    <span class="footer__item"><svg class="footer__icon" viewBox="0 0 16 16"><circle cx="8" cy="8" r="8" fill="#fff"/><path d="M5 4l2 2-1 1c.5 1.2 1.5 2.2 2.8 2.8l1-1 2 2-1.2 1.2C7.5 12 4 8.5 3.8 5.2z" fill="#000"/></svg>1300 462 718</span>
    <span class="footer__item"><svg class="footer__icon" viewBox="0 0 16 16"><circle cx="8" cy="8" r="7" fill="none" stroke="#fff" stroke-width="2"/><path d="M1 8h14M8 1c3 3 3 11 0 14M8 1c-3 3-3 11 0 14" stroke="#fff" fill="none"/></svg>www.stocklyz5.com.au</span>
    <span class="footer__item"><svg class="footer__icon" viewBox="0 0 16 16"><circle cx="8" cy="8" r="8" fill="#fff"/><rect x="4" y="5" width="8" height="6" fill="none" stroke="#000"/><path d="M4 5l4 3 4-3" fill="none" stroke="#000"/></svg>admin@stocklyz5.com.au</span>
  </footer>
</section>

<section class="flyer flyer--back">
  <div class="deco-circle" style="left:-40px;top:300px;width:140px;height:140px;background:#c9ebfa"></div>
  <div class="deco-circle" style="left:420px;top:680px;width:160px;height:160px;background:#c9ebfa"></div>
  <div class="back-header"></div>
  <div class="deco-circle" style="left:325px;top:0;width:190px;height:145px;background:#0d2a3a"></div>
  <div class="brand" style="left:48px;top:75px"><span>STOCKLY Z5</span><span class="brand__dot"></span></div>

  <div class="card" style="left:34px;top:188px">
    <div class="card__top">
      <div class="card__price"><span class="card__cur">$</span><span class="card__amount">9<sup>95</sup></span><span class="card__per">PER WEEK</span></div>
      <div class="card__name"><div class="card__title">SMALL RETAIL</div><div class="card__sub">SOFTWARE PACKAGE</div></div>
    </div>
    <ul class="card__list">
      <li><svg class="tick" viewBox="0 0 14 14"><circle cx="7" cy="7" r="7" fill="#fff"/><path d="M4 7l2 2 4-4" stroke="#1aa7e8" stroke-width="2" fill="none"/></svg>1-2 Staff Users</li>
      <li><svg class="tick" viewBox="0 0 14 14"><circle cx="7" cy="7" r="7" fill="#fff"/><path d="M4 7l2 2 4-4" stroke="#1aa7e8" stroke-width="2" fill="none"/></svg>1 Cash Register</li>
      <li><svg class="tick" viewBox="0 0 14 14"><circle cx="7" cy="7" r="7" fill="#fff"/><path d="M4 7l2 2 4-4" stroke="#1aa7e8" stroke-width="2" fill="none"/></svg>1 Store Location</li>
    </ul>
    <div class="card__buy">BUY NOW</div>
    <div class="card__tax">100% TAX DEDUCTIBLE<br>(Invoiced Monthly)</div>
  </div>

  <div class="card" style="left:264px;top:188px">
    <div class="card__top">
      <div class="card__price"><span class="card__cur">$</span><span class="card__amount">17<sup>95</sup></span><span class="card__per">PER WEEK</span></div>
      <div class="card__name"><div class="card__title">MEDIUM RETAIL</div><div class="card__sub">SOFTWARE PACKAGE</div></div>
    </div>
    <ul class="card__list">
      <li><svg class="tick" viewBox="0 0 14 14"><circle cx="7" cy="7" r="7" fill="#fff"/><path d="M4 7l2 2 4-4" stroke="#1aa7e8" stroke-width="2" fill="none"/></svg>3-8 Staff Users</li>
      <li><svg class="tick" viewBox="0 0 14 14"><circle cx="7" cy="7" r="7" fill="#fff"/><path d="M4 7l2 2 4-4" stroke="#1aa7e8" stroke-width="2" fill="none"/></svg>2-3 Cash Registers</li>
      <li><svg class="tick" viewBox="0 0 14 14"><circle cx="7" cy="7" r="7" fill="#fff"/><path d="M4 7l2 2 4-4" stroke="#1aa7e8" stroke-width="2" fill="none"/></svg>1 Store Location</li>
    </ul>
    <div class="card__buy">BUY NOW</div>
    <div class="card__tax">100% TAX DEDUCTIBLE<br>(Invoiced Monthly)</div>
  </div>

  <div class="card" style="left:34px;top:572px">
    <div class="card__top">
      <div class="card__price"><span class="card__cur">$</span><span class="card__amount">34<sup>95</sup></span><span class="card__per">PER WEEK</span></div>
      <div class="card__name"><div class="card__title">LARGE RETAIL</div><div class="card__sub">SOFTWARE PACKAGE</div></div>
    </div>
    <ul class="card__list">
      <li><svg class="tick" viewBox="0 0 14 14"><circle cx="7" cy="7" r="7" fill="#fff"/><path d="M4 7l2 2 4-4" stroke="#1aa7e8" stroke-width="2" fill="none"/></svg>8-20 Staff Users</li>
      <li><svg class="tick" viewBox="0 0 14 14"><circle cx="7" cy="7" r="7" fill="#fff"/><path d="M4 7l2 2 4-4" stroke="#1aa7e8" stroke-width="2" fill="none"/></svg>2-10 Cash Registers</li>
      <li><svg class="tick" viewBox="0 0 14 14"><circle cx="7" cy="7" r="7" fill="#fff"/><path d="M4 7l2 2 4-4" stroke="#1aa7e8" stroke-width="2" fill="none"/></svg>1 Store Location</li>
    </ul>
    <div class="card__buy">BUY NOW</div>
    <div class="card__tax">100% TAX DEDUCTIBLE<br>(Invoiced Monthly)</div>
  </div>

  <div class="card" style="left:264px;top:572px">
    <div class="card__top">
      <div class="card__price"><span class="card__cur">$</span><span class="card__amount">49<sup>95</sup></span><span class="card__per">PER WEEK</span></div>
      <div class="card__name"><div class="card__title">ENTERRISE</div><div class="card__sub">SOFTWARE PACKAGE</div></div>
    </div>
    <ul class="card__list">
      <li><svg class="tick" viewBox="0 0 14 14"><circle cx="7" cy="7" r="7" fill="#fff"/><path d="M4 7l2 2 4-4" stroke="#1aa7e8" stroke-width="2" fill="none"/></svg>20+ Staff Users</li>
      <li><svg class="tick" viewBox="0 0 14 14"><circle cx="7" cy="7" r="7" fill="#fff"/><path d="M4 7l2 2 4-4" stroke="#1aa7e8" stroke-width="2" fill="none"/></svg>10+ Cash Registers</li>
      <li><svg class="tick" viewBox="0 0 14 14"><circle cx="7" cy="7" r="7" fill="#fff"/><path d="M4 7l2 2 4-4" stroke="#1aa7e8" stroke-width="2" fill="none"/></svg>2-3 Store Locations</li>
    </ul>
    <div class="card__buy">BUY NOW</div>
    <div class="card__tax">100% TAX DEDUCTIBLE<br>(Invoiced Monthly)</div>
  </div>

  <footer class="footer">
    <span class="footer__item"><svg class="footer__icon" viewBox="0 0 16 16"><circle cx="8" cy="8" r="8" fill="#fff"/><path d="M5 4l2 2-1 1c.5 1.2 1.5 2.2 2.8 2.8l1-1 2 2-1.2 1.2C7.5 12 4 8.5 3.8 5.2z" fill="#000"/></svg>1300 462 718</span>
    <span class="footer__item"><svg class="footer__icon" viewBox="0 0 16 16"><circle cx="8" cy="8" r="7" fill="none" stroke="#fff" stroke-width="2"/><path d="M1 8h14M8 1c3 3 3 11 0 14M8 1c-3 3-3 11 0 14" stroke="#fff" fill="none"/></svg>www.stocklyz5.com.au</span>
    <span class="footer__item"><svg class="footer__icon" viewBox="0 0 16 16"><circle cx="8" cy="8" r="8" fill="#fff"/><rect x="4" y="5" width="8" height="6" fill="none" stroke="#000"/><path d="M4 5l4 3 4-3" fill="none" stroke="#000"/></svg>admin@stocklyz5.com.au</span>
  </footer>
</section>

</body>
</html>
```